Typing Service Business Card Design

Need a new business card design for new logo update. The Keyline Crew is an outsourced typing service. We type audio / voice files into word documents. We are a professional service that is recognised in the industry over the past 15 years and have a strong connection to our brand. The final design should be professional, simple, yet effective.

Business

Contact Information for Business Card

Rosalind Varga
Director

rosalind@kbq.com.au
www.thekeylinecrewbase.com.au

```html
<!DOCTYPE html>
<html lang="en">
<head>
<meta charset="utf-8">
<title>The Keyline Crew – Business Card</title>
<link rel="stylesheet" href="https://fonts.googleapis.com/css2?family=Roboto+Condensed:wght@300;400&family=Open+Sans:wght@400;600&display=swap">
<style>
  :root {
    --backdrop: #3a322e;
    --card: #1b1b1b;
    --magenta: #d94fb4;
    --white: #f4f4f4;
  }
  * { box-sizing: border-box; margin: 0; padding: 0; }
  html, body {
    width: 1200px; height: 780px; overflow: hidden;
    background: var(--backdrop);
  }
  .canvas {
    width: 1200px; height: 780px;
    display: flex; align-items: center; justify-content: center; gap: 40px;
  }
  .card {
    position: relative;
    width: 540px; height: 310px;
    background: var(--card);
    box-shadow: 0 10px 24px rgba(0,0,0,0.45);
  }
  .brand {
    display: flex; align-items: center; gap: 10px;
    font-family: "Roboto Condensed", sans-serif;
    font-weight: 400;
    color: var(--magenta);
    line-height: 1;
    white-space: nowrap;
  }
  .brand-mark { background: var(--magenta); flex: none; }
  .tagline {
    font-family: "Roboto Condensed", sans-serif;
    font-weight: 300;
    color: var(--white);
    line-height: 1;
    white-space: nowrap;
  }

  /* Contact side */
  .card--contact .brand { position: absolute; left: 40px; top: 42px; font-size: 34px; }
  .card--contact .brand-mark { width: 16px; height: 16px; }
  .card--contact .tagline { position: absolute; left: 66px; top: 88px; font-size: 20px; }
  .contact {
    position: absolute; right: 40px; bottom: 36px;
    text-align: right;
    font-family: "Open Sans", sans-serif;
  }
  .contact-name { color: var(--magenta); font-size: 24px; font-weight: 400; line-height: 1.1; }
  .contact-role { color: var(--white); font-size: 16px; font-weight: 600; margin-bottom: 16px; }
  .contact-line {
    display: flex; justify-content: flex-end; align-items: center; gap: 10px;
    color: var(--white); font-size: 14px; line-height: 1.6;
  }
  .contact-icon { width: 14px; height: 14px; flex: none; }

  /* Brand side */
  .card--brand { display: flex; flex-direction: column; align-items: center; justify-content: center; }
  .card--brand .brand { font-size: 48px; }
  .card--brand .brand-mark { width: 22px; height: 22px; }
  .card--brand .tagline { font-size: 26px; margin-top: 14px; margin-left: 40px; }
</style>
</head>
<body>
<main class="canvas">
  <section class="card card--contact">
    <div class="brand"><span class="brand-mark"></span>The Keyline Crew</div>
    <p class="tagline">Say it. We key it.</p>
    <div class="contact">
      <p class="contact-name">Rosalind Varga</p>
      <p class="contact-role">Director</p>
      <p class="contact-line">rosalind@kbq.com.au
        <svg class="contact-icon" viewBox="0 0 14 14" aria-hidden="true">
          <rect width="14" height="14" rx="2" fill="#d94fb4"/>
          <rect x="3" y="4" width="8" height="6" fill="none" stroke="#1b1b1b" stroke-width="1.2"/>
          <path d="M3 4 L7 7.5 L11 4" fill="none" stroke="#1b1b1b" stroke-width="1.2"/>
        </svg>
      </p>
      <p class="contact-line">www.thekeylinecrewbase.com.au
        <svg class="contact-icon" viewBox="0 0 14 14" aria-hidden="true">
          <rect width="14" height="14" rx="2" fill="#d94fb4"/>
          <circle cx="7" cy="7" r="3.8" fill="none" stroke="#1b1b1b" stroke-width="1.2"/>
          <path d="M3.2 7 H10.8 M7 3.2 V10.8" stroke="#1b1b1b" stroke-width="1"/>
        </svg>
      </p>
    </div>
  </section>

  <section class="card card--brand">
    <div class="brand"><span class="brand-mark"></span>The Keyline Crew</div>
    <p class="tagline">Say it. We key it.</p>
  </section>
</main>
</body>
</html>
```